International Insurance MGA needs a new Tradeshow Display Design

We need a new design for our tradeshow display. We are an Insurance MGA and we constantly attend several tradeshows throughout USA were we need to exhibit our company and products to insurance agents. The objective is to appoint new agents to sell our products as well as to remind our current agents of what we do and what we offer. We specialize in Mexican Insurance for American Residents, which they can only buy through their insurance agents. Therefore, the display is not meant for the general public but only for Insurance Agents

We have a blank display that has an available art size of 103.84" width by 89.12” height. This display needs to have a blank rectangular space of 36.8”by 49.04” by 61.36” to project a video. There is no restriction of where this blank space has to be on the display (left, center or right). Anything else outside the video space should be used for this design project. Please see attached file with details of the size and specifications/requirements.

Other important information about our company and services:

1. Our main colors are blue and white.

2. Our products are divided in Personal Lines (Auto, Homes and Boats) and Commercial Lines (Business Auto, Commercial Packages and Umbrellas).

3. We offer American Standards of coverage

4. Our Agents (TerraVel Producers) can manage their clients online as well as quote, bind, pay, endorse and cancel through our online platform.

5. The design should communicate to agents in some way the opportunity to sell Mexican Insurance to their clients, with the best commissions and the best coverages in the market, and with policies designed to look and read like American policies, hence our motto (the American Way).

6. Some elements we would like to see in the design are:

- Our logo
- Our motto (Mexican Insurance...the American Way!)
- Some type of representation of our products (detailed above) and our opportunities (best commissions, best companies, etc).
- The Insurance Companies we use (Top International Markets). See attached logos.
• ORLA Seguros
• KUV Mexico
• EZO Renovando las gestiones
• PRELT
• DSL Grupo Federal Comarcal
• BWT
- TerraVel Company Info
• www.terravel.example
• 1-800-TERRAVL

Please let us know if you have any questions.

Thanks!

```html
<!DOCTYPE html>
<html lang="en">
<head>
<meta charset="utf-8">
<title>TerraVel Tradeshow Display</title>
<link rel="stylesheet" href="https://fonts.googleapis.com/css2?family=Bebas+Neue&family=Roboto+Condensed:ital,wght@1,700&display=swap">
<style>
  :root {
    --sky: #3fb0ea;
    --blue: #1c6fc0;
    --navy: #0a2f6b;
    --deep: #061a44;
    --frame: #0b3f86;
    --white: #ffffff;
    --band: #eef0f2;
    --rule: #29a9e6;
    --brand: #2a2f8f;
    --grey: #5a5d63;
    --tick: #4cc3f5;
  }
  html, body { margin: 0; padding: 0; overflow: hidden; }
  body { width: 1200px; height: 1017px; background: var(--white); }
  .display {
    position: relative; width: 1200px; height: 1017px; overflow: hidden;
    font-family: 'Bebas Neue', 'Oswald', sans-serif;
  }
  .hero {
    position: absolute; left: 0; top: 0; width: 1200px; height: 778px;
    background:
      radial-gradient(ellipse 700px 520px at 180px 160px, var(--sky) 0%, rgba(63,176,234,0) 75%),
      linear-gradient(160deg, var(--blue) 0%, var(--navy) 60%, var(--deep) 100%);
  }
  .hero-rule { position: absolute; left: 0; top: 778px; width: 1200px; height: 9px; background: var(--rule); }
  .motto {
    position: absolute; left: 24px; top: 30px; margin: 0;
    color: var(--white); font-size: 82px; line-height: 76px; font-weight: 400;
    letter-spacing: 0.5px; text-shadow: 0 3px 6px rgba(0,0,0,0.35);
  }
  .family-photo {
    position: absolute; left: 0; top: 308px; width: 640px; height: 470px;
    background: radial-gradient(ellipse 330px 240px at 300px 250px, #d9c2b0 0%, #b59884 45%, rgba(120,150,190,0.6) 80%, rgba(40,110,190,0) 100%);
  }
  .video-screen {
    position: absolute; left: 554px; top: 14px; width: 624px; height: 462px;
    background: var(--white); border: 10px solid var(--frame);
  }
  .product-lines { position: absolute; top: 562px; display: flex; gap: 38px; left: 618px; }
  .line-group h2 {
    margin: 0; color: var(--white); font-size: 37px; line-height: 35px; font-weight: 400; white-space: nowrap;
  }
  .line-group ul { list-style: none; margin: 0; padding: 0; }
  .line-group li {
    color: var(--white); font-size: 37px; line-height: 35px; display: flex; align-items: center; gap: 3px; white-space: nowrap;
  }
  .line-group li svg { width: 17px; height: 17px; flex: none; }
  .partners-band { position: absolute; left: 0; top: 787px; width: 1200px; height: 230px; background: var(--band); }
  .carrier {
    position: absolute; display: flex; align-items: center; gap: 10px;
    color: var(--brand); font-size: 56px; line-height: 1; white-space: nowrap;
  }
  .carrier .mark { width: 26px; height: 26px; background: var(--brand); }
  .carrier.small { font-size: 42px; }
  .carrier.small .mark { width: 20px; height: 20px; }
  .brand {
    position: absolute; left: 700px; top: 818px; color: var(--brand);
    font-family: 'Roboto Condensed', 'Arial Narrow', sans-serif;
  }
  .brand-name { font-size: 88px; font-weight: 700; font-style: italic; line-height: 1; letter-spacing: -1px; margin: 0; }
  .brand-sub { font-size: 26px; font-weight: 700; font-style: italic; margin: 4px 0 0 12px; white-space: nowrap; }
  .contact {
    position: absolute; left: 700px; top: 966px; display: flex; gap: 18px; align-items: center;
    color: var(--grey); font-size: 32px; line-height: 1; white-space: nowrap;
  }
  .contact span { display: flex; align-items: center; gap: 5px; white-space: nowrap; }
  .contact svg { width: 24px; height: 24px; flex: none; }
</style>
</head>
<body>
<main class="display">
  <section class="hero">
    <h1 class="motto">Mexican<br>Insurance...<br>The American Way!</h1>
    <div class="family-photo" role="img" aria-label="Photo of a smiling family of five posing together on a sofa"></div>
    <div class="video-screen" aria-label="Video projection area"></div>
    <div class="product-lines">
      <div class="line-group">
        <h2>Personal Lines:</h2>
        <ul>
          <li><svg viewBox="0 0 16 16"><path d="M2 8.5l4 4 8-9" fill="none" stroke="var(--tick)" stroke-width="2.6"/></svg>Auto</li>
          <li><svg viewBox="0 0 16 16"><path d="M2 8.5l4 4 8-9" fill="none" stroke="var(--tick)" stroke-width="2.6"/></svg>Homes</li>
          <li><svg viewBox="0 0 16 16"><path d="M2 8.5l4 4 8-9" fill="none" stroke="var(--tick)" stroke-width="2.6"/></svg>Boats</li>
        </ul>
      </div>
      <div class="line-group">
        <h2>Commercial Lines</h2>
        <ul>
          <li><svg viewBox="0 0 16 16"><path d="M2 8.5l4 4 8-9" fill="none" stroke="var(--tick)" stroke-width="2.6"/></svg>Business Auto</li>
          <li><svg viewBox="0 0 16 16"><path d="M2 8.5l4 4 8-9" fill="none" stroke="var(--tick)" stroke-width="2.6"/></svg>Commercial Packages</li>
          <li><svg viewBox="0 0 16 16"><path d="M2 8.5l4 4 8-9" fill="none" stroke="var(--tick)" stroke-width="2.6"/></svg>Umbrellas</li>
        </ul>
      </div>
    </div>
  </section>
  <div class="hero-rule"></div>

  <footer class="partners-band">
    <div class="carrier" style="left:24px; top:42px;"><span class="mark"></span>DSL</div>
    <div class="carrier" style="left:282px; top:42px;"><span class="mark"></span>PRELT</div>
    <div class="carrier" style="left:452px; top:42px;"><span class="mark"></span>ORLA</div>
    <div class="carrier small" style="left:24px; top:152px;"><span class="mark"></span>EZO</div>
    <div class="carrier small" style="left:282px; top:152px;"><span class="mark"></span>KUV</div>
    <div class="carrier small" style="left:452px; top:152px;"><span class="mark"></span>BWT</div>
  </footer>

  <div class="brand">
    <p class="brand-name">TerraVel</p>
    <p class="brand-sub">International Insurance Services, LLC</p>
  </div>
  <div class="contact">
    <span>www.terravel.example</span>
    <span><svg viewBox="0 0 24 24"><path d="M6.6 10.8a15 15 0 0 0 6.6 6.6l2.2-2.2a1 1 0 0 1 1-.25 11.4 11.4 0 0 0 3.6.57 1 1 0 0 1 1 1V20a1 1 0 0 1-1 1A17 17 0 0 1 3 4a1 1 0 0 1 1-1h3.5a1 1 0 0 1 1 1c0 1.25.2 2.45.57 3.57a1 1 0 0 1-.25 1z" fill="var(--brand)"/></svg>1-800-TERRAVL</span>
  </div>
</main>
</body>
</html>
```